Swim school needs flyer design

Need revamp of flyer design. Attached last years flyer (BCP A4 Holiday Leaflet-v6.2 (1)). Also attached is this years information in word format (BCP A4 BCP & Holiday Leaflet 2014-2015).
This flyer must fit with our logo (Blue Current Pools-RGB). This flyer is our first point of call for many of our clients. With the amount of information that must be provided, it is important that it flows and is appealing. Photos can be accessed from http://kemapics.brightfolio.net/apps/photos/album?albumid=52930417 or from your own source
Important that the final design fits printers template.(Flyers-A4-210x297mm-2Side - attached)

```html
<!DOCTYPE html>
<html lang="en">
<head>
<meta charset="utf-8">
<title>Holiday Swim Classes – Blue Current Pools</title>
<link rel="stylesheet" href="https://fonts.googleapis.com/css2?family=Open+Sans:ital,wght@0,400;0,600;0,700;1,400;1,600;1,700;1,800&family=Arimo:wght@400;700&display=swap">
<style>
  :root {
    --orange: #f0941f;
    --yellow: #fbb817;
    --lime: #b3cb2d;
    --sky: #12a9d4;
    --white: #ffffff;
    --paper: #f3f1ec;
    --ink: #333333;
    --ink-soft: #555555;
    --card: rgba(232, 232, 220, 0.92);
    --backdrop: #e9e6e2;
  }
  * { box-sizing: border-box; margin: 0; padding: 0; }
  html, body { width: 1040px; height: 1200px; overflow: hidden; }
  body {
    background: var(--backdrop);
    font-family: "Open Sans", Arial, sans-serif;
    position: relative;
  }
  .flyer {
    position: absolute;
    left: 70px; top: 18px;
    width: 900px; height: 1164px;
    overflow: hidden;
    background: var(--white);
    box-shadow: 0 6px 24px rgba(0,0,0,0.18);
  }
  .flyer-shapes { position: absolute; inset: 0; }

  .headline {
    position: absolute;
    top: 26px; left: 0; width: 100%;
    text-align: center;
    color: var(--white);
    font-style: italic; font-weight: 700;
    font-size: 66px; letter-spacing: 0.5px;
  }

  .schedule {
    position: absolute;
    left: 22px; top: 124px;
    width: 482px; height: 306px;
    background: var(--yellow);
    border: 3px solid var(--white);
    transform: rotate(-1.4deg);
    box-shadow: 2px 3px 6px rgba(0,0,0,0.25);
    font-family: "Arimo", Arial, sans-serif;
    padding: 8px 0 8px 0;
  }
  .schedule-row {
    position: relative;
    height: 36px;
    margin-left: 138px;
    margin-right: 6px;
    display: flex; align-items: center; justify-content: center;
    font-size: 22px; color: #222;
  }
  .schedule-row.is-light { background: var(--paper); margin-left: 130px; }
  .schedule-year {
    position: absolute;
    left: 26px;
    font-family: "Arimo", Arial, sans-serif;
    font-weight: 700; font-size: 26px; color: var(--white);
  }
  .schedule-year.y2014 { top: 50px; }
  .schedule-year.y2015 { top: 160px; }

  .call-badge {
    position: absolute;
    left: 590px; top: 132px;
    width: 292px; height: 292px;
    border-radius: 50%;
    background: var(--sky);
    border: 8px solid var(--white);
    color: var(--white);
    text-align: center;
    font-style: italic;
    display: flex; flex-direction: column; justify-content: center; align-items: center;
  }
  .call-badge .call-title { font-weight: 700; font-size: 42px; line-height: 1.1; }
  .call-badge .call-number { font-weight: 600; font-size: 50px; line-height: 1.1; letter-spacing: 1px; }
  .call-badge .call-note { font-weight: 700; font-size: 17px; margin-top: 8px; }

  .pool-card {
    position: absolute;
    left: 29px; top: 462px;
    width: 304px; height: 362px;
    background: var(--card);
    border: 3px solid rgba(255,255,255,0.85);
    padding: 0 18px;
    color: var(--ink);
  }
  .pool-photo {
    position: absolute;
    left: 36px; top: 12px;
    width: 222px; height: 134px;
    transform: rotate(-2.5deg);
    background: linear-gradient(160deg, #5cc0e6 0%, #1e9fd4 45%, #f0b88a 70%, #2a8fcf 100%);
    box-shadow: 1px 2px 4px rgba(0,0,0,0.3);
  }
  .pool-card h2 {
    margin-top: 172px;
    font-style: italic; font-weight: 700;
    font-size: 21px; color: var(--ink);
  }
  .pool-card .pool-facts {
    font-style: italic; font-size: 12.5px; line-height: 1.35; margin-top: 2px;
  }
  .pool-card .pool-terms {
    font-style: italic; font-size: 14px; line-height: 1.35; margin-top: 18px;
  }

  .notice {
    position: absolute;
    left: 677px; top: 0;
  }
  .important {
    position: absolute;
    left: 411px; top: 612px;
    width: 470px;
    color: var(--white);
  }
  .important h2 {
    font-style: italic; font-weight: 700; font-size: 35px; line-height: 1.1;
    margin-bottom: 8px;
  }
  .important-columns { display: flex; gap: 22px; }
  .important ul {
    list-style: none;
    font-style: italic; font-weight: 600;
    font-size: 14.5px; line-height: 1.32;
  }
  .important ul.col-a { width: 255px; }
  .important ul.col-b { width: 200px; margin-top: -2px; }
  .important li::before { content: "• "; }

  .web-address {
    position: absolute;
    left: 0; top: 870px; width: 100%;
    text-align: center;
    color: var(--white);
    font-style: italic; font-weight: 700;
    font-size: 52px; letter-spacing: 0.5px;
  }

  .venues {
    position: absolute;
    left: 67px; top: 1004px;
    color: var(--ink);
    font-style: italic; font-size: 18.5px; line-height: 1.3;
  }
  .venues .venue + .venue { margin-top: 24px; }
  .venues .venue-name { font-weight: 700; }
  .venues .venue-address { color: var(--ink-soft); font-weight: 600; }

  .brand {
    position: absolute;
    right: 40px; top: 1030px;
    display: flex; align-items: center; gap: 14px;
  }
  .brand-dot {
    width: 46px; height: 46px; border-radius: 50%;
    background: var(--orange);
  }
  .brand-name {
    color: var(--sky);
    font-family: "Open Sans", Arial, sans-serif;
    font-weight: 600; font-size: 44px; line-height: 1;
  }
</style>
</head>
<body>
  <main class="flyer">
    <svg class="flyer-shapes" width="900" height="1164" viewBox="0 0 900 1164" aria-hidden="false">
      <defs>
        <linearGradient id="swimmer-tones" x1="0" y1="0" x2="1" y2="1">
          <stop offset="0" stop-color="#c9b9ad"/>
          <stop offset="0.35" stop-color="#d8c3b4"/>
          <stop offset="0.6" stop-color="#b65a4f"/>
          <stop offset="0.8" stop-color="#d7c6b8"/>
          <stop offset="1" stop-color="#cbbcae"/>
        </linearGradient>
      </defs>
      <rect class="band-orange" x="0" y="0" width="900" height="600" fill="var(--orange)"/>
      <g role="img" aria-label="Photo of a child in goggles swimming underwater towards the camera">
        <path d="M0,170 C250,140 600,100 900,148 L900,600 L0,600 Z" fill="url(#swimmer-tones)"/>
      </g>
      <path d="M0,170 C250,140 600,100 900,148" fill="none" stroke="var(--white)" stroke-width="4"/>
      <path d="M0,588 C240,600 560,575 900,528 L900,845 L0,845 Z" fill="var(--lime)"/>
      <path d="M0,588 C240,600 560,575 900,528" fill="none" stroke="var(--white)" stroke-width="4"/>
      <path d="M0,854 C300,848 600,846 900,840 L900,968 L0,968 Z" fill="var(--sky)"/>
    </svg>

    <h1 class="headline">Holiday Swim Classes</h1>

    <section class="schedule" aria-label="Holiday program dates">
      <span class="schedule-year y2014">2014</span>
      <span class="schedule-year y2015">2015</span>
      <div class="schedule-row">Sep 23rd – 27th</div>
      <div class="schedule-row is-light">Sep 30th – Oct 4th</div>
      <div class="schedule-row">Jan 6th – 10th</div>
      <div class="schedule-row is-light">Jan 13th – 17th</div>
      <div class="schedule-row">Jan 20th – 24th</div>
      <div class="schedule-row is-light">Mar 30th – Apr 3rd</div>
      <div class="schedule-row">Apr 6th – 10th</div>
      <div class="schedule-row is-light">Jun 29th – Jul 3rd</div>
    </section>

    <aside class="call-badge">
      <span class="call-title">Call now!</span>
      <span class="call-number">9460 2718</span>
      <span class="call-note">Limited places only..</span>
    </aside>

    <section class="pool-card">
      <div class="pool-photo" role="img" aria-label="Photo of a smiling child in a swim cap and goggles underwater"></div>
      <h2>Salt Water Pool</h2>
      <p class="pool-facts">Ages 3 and older<br>$75 per child per week<br>(5x½ hour classes per week)</p>
      <p class="pool-terms">No bookings are taken without a fully completed enrolment form and payment.<br>Places are limited so book early to avoid disappointment.</p>
    </section>

    <section class="important">
      <h2>Important</h2>
      <div class="important-columns">
        <ul class="col-a">
          <li>All holiday swim classes are conducted at the Elmwood primary school pool</li>
          <li>30 minute classes run every ½ hour from 9.30am to 12 noon</li>
          <li>Limited places due to small class</li>
        </ul>
        <ul class="col-b">
          <li>Beginners to advanced swimmers welcome</li>
          <li>All children are grouped by age and ability</li>
          <li>No refunds or makeups for holiday programs</li>
        </ul>
      </div>
    </section>

    <p class="web-address">www.bluecurrentpools.com.au</p>

    <footer class="venues">
      <div class="venue">
        <div class="venue-name">Elmwood P.S. Pool</div>
        <div class="venue-address">42 Ferris Street Elmwood</div>
      </div>
      <div class="venue">
        <div class="venue-name">Ridgeview College Pool</div>
        <div class="venue-address">Gate 1, Kestrel St Ridgeview</div>
      </div>
    </footer>

    <div class="brand">
      <span class="brand-dot"></span>
      <span class="brand-name">Blue Current Pools</span>
    </div>
  </main>
</body>
</html>
```